Business cards for Remote DBA team

Business cards for team offering database administration, consultation, machine learning and AI services. As of now team is using both
www.korvilnet.cz and www.brestmoorlab.cz URLs

Target Market(s)

IT managers

Industry/Entity Type

It Professional

Contact Information for Business Card

Should include logo
name, email, phone, twitter tag

Font styles to use
Sans Serif

Colors

Designer to choose colors to be used in the design.

```html
<!DOCTYPE html>
<html lang="en">
<head>
<meta charset="utf-8">
<title>Korvilnet Business Card</title>
<link rel="stylesheet" href="https://fonts.googleapis.com/css2?family=Roboto:wght@400;500;700&display=swap">
<style>
  :root {
    --page-bg: #ecebe8;
    --card-bg: #ffffff;
    --brand-blue: #1b8ac9;
    --text-grey: #444a50;
  }
  html, body {
    margin: 0;
    padding: 0;
    width: 1200px;
    height: 989px;
    overflow: hidden;
    background: var(--page-bg);
    font-family: "Roboto", Arial, sans-serif;
  }
  .business-card {
    position: absolute;
    left: 50px;
    top: 178px;
    width: 1100px;
    height: 632px;
    background: var(--card-bg);
  }
  .brand {
    position: absolute;
    left: 0;
    right: 0;
    top: 160px;
    display: flex;
    justify-content: center;
    align-items: center;
    gap: 22px;
  }
  .brand-dot {
    width: 46px;
    height: 46px;
    border-radius: 50%;
    background: var(--brand-blue);
  }
  .brand-name {
    font-weight: 700;
    font-size: 82px;
    letter-spacing: 1px;
    color: var(--brand-blue);
    line-height: 1;
  }
  .holder-name {
    position: absolute;
    left: 52px;
    top: 452px;
    margin: 0;
    font-weight: 500;
    font-size: 40px;
    color: var(--brand-blue);
    letter-spacing: 0.3px;
  }
  .contact-list {
    position: absolute;
    left: 682px;
    top: 406px;
    margin: 0;
    padding: 0;
    list-style: none;
  }
  .contact-item {
    display: flex;
    align-items: center;
    height: 35.5px;
    font-size: 26px;
    color: var(--text-grey);
  }
  .contact-icon {
    width: 26px;
    height: 26px;
    margin-right: 16px;
    fill: var(--brand-blue);
    flex: none;
  }
</style>
</head>
<body>
  <section class="business-card">
    <div class="brand">
      <span class="brand-dot"></span>
      <span class="brand-name">KORVILNET</span>
    </div>

    <h1 class="holder-name">TOMAS HALVEK</h1>

    <ul class="contact-list">
      <li class="contact-item">
        <svg class="contact-icon" viewBox="0 0 24 24"><path d="M6.6 10.8c1.4 2.8 3.8 5.1 6.6 6.6l2.2-2.2c.3-.3.7-.4 1-.2 1.1.4 2.3.6 3.6.6.6 0 1 .4 1 1V20c0 .6-.4 1-1 1C10.6 21 3 13.4 3 4c0-.6.4-1 1-1h3.5c.6 0 1 .4 1 1 0 1.3.2 2.5.6 3.6.1.3 0 .7-.2 1z"/></svg>
        555 201 7346
      </li>
      <li class="contact-item">
        <svg class="contact-icon" viewBox="0 0 24 24"><path d="M2 5h20v14H2z M3.5 6.5 12 13l8.5-6.5" fill="none" stroke="#1b8ac9" stroke-width="2"/></svg>
        info@korvilnet.com
      </li>
      <li class="contact-item">
        <svg class="contact-icon" viewBox="0 0 24 24"><circle cx="12" cy="12" r="10" fill="none" stroke="#1b8ac9" stroke-width="2.4"/><path d="M6 8c2 0 3 1 3 3s2 2 2 4-1 3-1 5M14 4c0 2 2 3 4 3s2 3 3 4"/><circle cx="9" cy="10" r="3"/><circle cx="16" cy="15" r="3"/></svg>
        www.brestmoorlab.cz
      </li>
      <li class="contact-item">
        <svg class="contact-icon" viewBox="0 0 24 24"><circle cx="12" cy="12" r="10"/></svg>
        www.korvilnet.cz
      </li>
    </ul>
  </section>
</body>
</html>
```